Australian Sports Podiatry Business needs a Vantor Games marketing flyer

The Stride Clinic is looking for a double sided DLflyer to send out to homes which is targeted at people interested in being fit and healthy. To include:

the Vantor Games logo and colours
sporty background

Are you Set For Vantor?
Whatever Your Goals, We'll Keep You On Track
National and International Sports Experience
Oberin Para Games (and logo if possible)
Tolvane Federation Games (and logo if poss)
Quillan Multisport Global Series (+logo)
Quillan Dravitz Shield Tennis (+logo)

The Stride Clinic name, logo, phone number 9271 6408, website www.harbelstride.net, email info@harbelstride.net

Dr Kamal Ratnavegar's Background:
Kamal's has 20 years experience in the field of Sports Medicine and lower limb biomechanics, and he has had extensive experience with treatment of elite athletes from the Southland Athletic Foundation, the College of Games, the Southland Gannets, Corvale Marauders and the Corvale Pelicans. He was also selected for the HVTB Medical Team to provide Podiatry Services at the Oberin 2000 Para Games, the 2000 GMX Global Multisport Series, the Tolvane 2006 Federation Games and the Quillan 2013 Dravitz Shield. Kamal now treats many athletes from all disciplines in Perth and surrounding areas.

In 1999 Kamal became the Director and Senior Podiatrist for The Stride Clinic in Perth, Western Australia. Since then he has also been a Director of Athletic Health Southland (AHS), WA Director for the Pacific Guild of Podiatric Sports Medicine (PGPSM), and an External Advisor to the Brindlemoor University’s Podiatric Medicine Unit. He is currently road testing minimalist running shoes for optimised performance and injury prevention.

Kamal has always been involved with high level sports, having held a 4x400m Australian Record and also played 1st Division Hockey. He is now training for the Veterans Track Global Meet in October, and volunteers at Kestrow Thunder Junior Runners. He also enjoys keeping fit by running after his 3 kids Mirela, Odette, and Felix.

Target Market(s)

People interested in being fit and healthy

Industry/Entity Type

Medical

Requirements
Must have
• To include:
• the Vantor Games logo and colours
• sporty background
• Are you Set For Vantor?
• Whatever Your Goals, We'll Keep You On Track
• National and International Sports Experience
• Oberin Para Games (and logo if possible)
• Tolvane Federation Games (and logo if poss)
• Quillan Multisport Global Series (+logo)
• Quillan Dravitz Shield Tennis (+logo)
• The Stride Clinic name, logo, phone number 9271 6408, website www.harbelstride.net, email info@harbelstride.net
• Dr Kamal Ratnavegar's Background:
• Kamal's has 20 years experience in the field of Sports Medicine and lower limb biomechanics, and he has had extensive experience with treatment of elite athletes from the Southland Athletic Foundation, the College of Games, the Southland Gannets, Corvale Marauders and the Corvale Pelicans. He was also selected for the HVTB Medical Team to provide Podiatry Services at the Oberin 2000 Para Games, the 2000 GMX Global Multisport Series, the Tolvane 2006 Federation Games and the Quillan 2013 Dravitz Shield. Kamal now treats many athletes from all disciplines in Perth and surrounding areas.
• In 1999 Kamal became the Director and Senior Podiatrist for The Stride Clinic in Perth, Western Australia. Since then he has also been a Director of Athletic Health Southland (AHS), WA Director for the Pacific Guild of Podiatric Sports Medicine (PGPSM), and an External Advisor to the Brindlemoor University’s Podiatric Medicine Unit. He is currently road testing minimalist running shoes for optimised performance and injury prevention.
Nice to have
• Kamal has always been involved with high level sports, having held a 4x400m Australian Record and also played 1st Division Hockey. He is now training for the Veterans Track Global Meet in October, and volunteers at Kestrow Thunder Junior Runners. He also enjoys keeping fit by running after his 3 kids Mirela, Odette, and Felix.

```html
<!DOCTYPE html>
<html lang="en">
<head>
<meta charset="utf-8">
<title>The Stride Clinic – DL Flyer</title>
<link rel="stylesheet" href="https://fonts.googleapis.com/css2?family=Anton&family=Montserrat:wght@500;600;700&family=Oswald:wght@600&family=Quicksand:wght@500&display=swap">
<style>
:root{
  --clinic-blue:#1a6fb8;
  --deep-blue:#0f5fa8;
  --orange:#f7941d;
  --green:#7dc242;
  --magenta:#e3177f;
  --teal:#14a89a;
  --wine:#5a0d1e;
  --ink:#ffffff;
  --grey:#6d6e71;
  --page:#ffffff;
}
*{margin:0;padding:0;box-sizing:border-box}
html,body{width:1200px;height:1000px;overflow:hidden;background:var(--page)}
.canvas{position:relative;width:1200px;height:1000px}
.panel{position:absolute;top:28px;width:464px;height:945px;overflow:hidden;background:#fff;box-shadow:0 0 6px rgba(0,0,0,.12)}
.panel--front{left:119px}
.panel--back{left:623px}
.shapes{position:absolute;left:0;top:0}

/* brand name */
.brand{position:absolute;display:flex;align-items:center;gap:10px;white-space:nowrap}
.brand-dot{flex:none;border-radius:50%;background:var(--clinic-blue)}
.brand-name{font-family:'Montserrat',sans-serif;font-weight:600;color:var(--clinic-blue)}
.brand-url{position:absolute;font-family:'Montserrat',sans-serif;font-weight:600;color:var(--grey);font-size:12px;letter-spacing:.3px}

/* front */
.photo-runners{position:absolute;left:0;top:0;width:464px;height:700px;
  background:linear-gradient(180deg,#f4f7f4 0%,#eef3ef 14%,#9fcf7a 28%,#5fa843 55%,#3d8a3a 100%)}
.headline{position:absolute;left:72px;top:270px;font-family:'Anton',sans-serif;color:var(--ink);
  font-size:56px;line-height:54px;text-transform:uppercase;transform:scaleX(1.28);transform-origin:left top}
.games-mark{position:absolute;left:66px;top:545px;width:120px;font-family:'Anton',sans-serif;
  color:var(--ink);font-size:28px;line-height:32px;text-transform:uppercase;text-align:center}
.slogan{position:absolute;left:0;top:678px;width:464px;text-align:center;font-family:'Anton',sans-serif;
  color:var(--ink);font-size:37px;line-height:35px;text-transform:uppercase;transform:skewX(-8deg)}
.experience-title{position:absolute;left:0;top:771px;width:464px;text-align:center;font-family:'Montserrat',sans-serif;
  font-weight:500;color:var(--ink);font-size:13.5px;letter-spacing:.4px}
.event{position:absolute;top:792px;width:112px;text-align:center}
.event-badge{width:38px;height:38px;margin:0 auto 10px;border-radius:50%;background:rgba(255,255,255,.85)}
.event-name{font-family:'Oswald',sans-serif;font-weight:600;color:var(--ink);font-size:10.5px;line-height:11px;text-transform:uppercase}
.contact{position:absolute;left:0;width:464px;display:flex;justify-content:center;gap:22px;
  font-family:'Montserrat',sans-serif;font-weight:600;color:var(--ink);font-size:15px}
.contact span{display:flex;align-items:center;gap:6px}
.contact svg{width:15px;height:15px}

/* back */
.photo-portrait{position:absolute;left:232px;top:30px;width:232px;height:400px;
  background:linear-gradient(180deg,#f4f4f4 0%,#e6e2de 40%,#f2f2f2 100%)}
.doctor-name{position:absolute;left:40px;top:278px;width:250px;text-align:center;font-family:'Montserrat',sans-serif;
  font-weight:700;color:var(--ink);font-size:23px;line-height:24px;text-transform:uppercase}
.doctor-role{position:absolute;left:40px;top:338px;width:250px;text-align:center;font-family:'Montserrat',sans-serif;
  font-weight:700;color:var(--orange);font-size:21px}
.bio{position:absolute;left:40px;top:406px;width:384px;font-family:'Quicksand',sans-serif;font-weight:500;
  color:var(--ink);font-size:12.6px;line-height:16px;letter-spacing:.15px;text-align:justify}
.bio p{margin-bottom:16px}
.photo-clinic{position:absolute;left:0;top:830px;width:464px;height:115px;
  background:linear-gradient(180deg,#3b1f5c 0%,#24123d 100%)}
.back-url{position:absolute;left:0;top:868px;width:464px;text-align:center;font-family:'Montserrat',sans-serif;
  font-weight:700;color:var(--ink);font-size:16px}
</style>
</head>
<body>
<div class="canvas">

  <section class="panel panel--front">
    <div class="photo-runners" role="img" aria-label="Photo of athletes running through a steeplechase water jump in a stadium"></div>
    <svg class="shapes" width="464" height="945" viewBox="0 0 464 945">
      <polygon points="0,142 240,272 0,320" fill="#f39a1e" opacity=".85"/>
      <polygon points="464,150 464,330 210,272" fill="#8cc63f" opacity=".75"/>
      <polygon points="0,650 464,662 464,742 0,767" fill="var(--wine)"/>
      <polygon points="0,650 464,662 464,690 0,684" fill="#8a1526" opacity=".7"/>
      <polygon points="0,767 464,742 464,882 0,882" fill="var(--magenta)"/>
      <rect x="0" y="882" width="464" height="63" fill="var(--teal)"/>
    </svg>

    <div class="brand" style="left:0;width:464px;justify-content:center;top:172px">
      <span class="brand-dot" style="width:18px;height:18px"></span>
      <span class="brand-name" style="font-size:23px">The Stride Clinic</span>
    </div>
    <div class="brand-url" style="left:0;width:464px;text-align:center;top:204px">www.harbelstride.net</div>

    <h1 class="headline">Are<br>You<br>Set<br>For</h1>
    <div class="games-mark">Vantor<br>Games</div>

    <p class="slogan">Whatever your goals,<br>we'll keep you on track</p>

    <p class="experience-title">NATIONAL AND INTERNATIONAL SPORTS EXPERIENCE</p>
    <div class="event" style="left:18px"><div class="event-badge"></div><div class="event-name">Oberin<br>Para Games</div></div>
    <div class="event" style="left:117px"><div class="event-badge"></div><div class="event-name">Tolvane<br>Federation<br>Games</div></div>
    <div class="event" style="left:229px"><div class="event-badge"></div><div class="event-name">Quillan<br>Multisport Global<br>Series</div></div>
    <div class="event" style="left:331px"><div class="event-badge"></div><div class="event-name">Quillan<br>Dravitz Shield<br>Tennis</div></div>

    <div class="contact" style="top:890px">
      <span><svg viewBox="0 0 24 24"><path d="M6.6 10.8a15.1 15.1 0 0 0 6.6 6.6l2.2-2.2a1 1 0 0 1 1-.25 11.4 11.4 0 0 0 3.6.57 1 1 0 0 1 1 1V20a1 1 0 0 1-1 1A17 17 0 0 1 3 4a1 1 0 0 1 1-1h3.5a1 1 0 0 1 1 1c0 1.25.2 2.45.57 3.57a1 1 0 0 1-.25 1z" fill="#fff"/></svg>9271 6408</span>
      <span><svg viewBox="0 0 24 24"><rect x="2" y="5" width="20" height="14" fill="none" stroke="#fff" stroke-width="1.8"/><path d="M2 5l10 8 10-8" fill="none" stroke="#fff" stroke-width="1.8"/></svg>info@harbelstride.net</span>
    </div>
  </section>

  <section class="panel panel--back">
    <div class="photo-portrait" role="img" aria-label="Portrait of the podiatrist in a white shirt and patterned tie"></div>
    <div class="photo-clinic" role="img" aria-label="Photo of a podiatry consultation in the clinic"></div>
    <svg class="shapes" width="464" height="945" viewBox="0 0 464 945">
      <polygon points="0,147 385,367 0,397" fill="var(--deep-blue)"/>
      <polygon points="0,397 464,352 464,862 0,832" fill="var(--orange)"/>
    </svg>

    <div class="brand" style="left:40px;top:140px">
      <span class="brand-dot" style="width:14px;height:14px"></span>
      <span class="brand-name" style="font-size:17px">The Stride Clinic</span>
    </div>

    <h2 class="doctor-name">Dr. Kamal<br>Ratnavegar</h2>
    <p class="doctor-role">Podiatrist</p>

    <div class="bio">
      <p>Kamal's has 20 years experience in the field of Sports Medicine and lower limb biomechanics, and he has had extensive experience with treatment of elite athletes from the Southland Athletic Foundation, the College of Games, the Southland Gannets, Corvale Marauders and the Corvale Pelicans. He was also selected for the HVTB Medical Team to provide Podiatry Services at the Oberin 2000 Para Games, the 2000 GMX Global Multisport Series, the Tolvane 2006 Federation Games and the Quillan 2013 Dravitz Shield. Kamal now treats many athletes from all disciplines in Perth and surrounding areas.</p>
      <p>In 1999 Kamal became the Director and Senior Podiatrist for The Stride Clinic in Perth, Western Australia. Since then he has also been a Director of Athletic Health Southland (AHS), WA Director for the Pacific Guild of Podiatric Sports Medicine (PGPSM), and an External Advisor to the Brindlemoor University’s Podiatric Medicine Unit. He is currently road testing minimalist running shoes for optimised performance and injury prevention.</p>
      <p>Kamal has always been involved with high level sports, having held a 4x400m Australian Record and also played 1st Division Hockey. He is now training for the Veterans Track Global Meet in October, and volunteers at Kestrow Thunder Junior Runners. He also enjoys keeping fit by running after his 3 kids Mirela, Odette, and Felix.</p>
    </div>

    <p class="back-url">www.harbelstride.net</p>
    <div class="contact" style="top:890px">
      <span><svg viewBox="0 0 24 24"><path d="M6.6 10.8a15.1 15.1 0 0 0 6.6 6.6l2.2-2.2a1 1 0 0 1 1-.25 11.4 11.4 0 0 0 3.6.57 1 1 0 0 1 1 1V20a1 1 0 0 1-1 1A17 17 0 0 1 3 4a1 1 0 0 1 1-1h3.5a1 1 0 0 1 1 1c0 1.25.2 2.45.57 3.57a1 1 0 0 1-.25 1z" fill="#fff"/></svg>9271 6408</span>
      <span><svg viewBox="0 0 24 24"><rect x="2" y="5" width="20" height="14" fill="none" stroke="#fff" stroke-width="1.8"/><path d="M2 5l10 8 10-8" fill="none" stroke="#fff" stroke-width="1.8"/></svg>info@harbelstride.net</span>
    </div>
  </section>

</div>
</body>
</html>
```